Realtor business card

Looking for a business card that will stand out from the rest. My area of expertise is residential real estate and loans.

Industry/Entity Type

Residential

Requirements
Must have
• Marcus Whitley, SFR
Broker
Mortgage Loan Originator
Notary Public
DRE License #07329184
NMLS 581706
Cell 714-552-0718
Fax 888-417-2965
www.marcuswhitleyhomes.example
mw@marcuswhitleyhomes.example

```html
<!DOCTYPE html>
<html lang="en">
<head>
<meta charset="utf-8">
<title>Marcus Whitley — Business Card</title>
<link rel="stylesheet" href="https://fonts.googleapis.com/css2?family=Oswald:wght@500&family=Lato:wght@400;700&display=swap">
<style>
  :root {
    --backdrop: #5a5a5a;
    --card-stock: #e9e9e9;
    --card-edge: #f4f4f4;
    --panel-grey: #d9d9d9;
    --brand-blue: #3468a8;
    --front-blue: #3f6699;
    --ink: #2b2b2b;
    --ink-soft: #6a6a6a;
    --white: #ffffff;
  }
  * { margin: 0; padding: 0; box-sizing: border-box; }
  html, body { width: 1200px; height: 717px; overflow: hidden; }
  body {
    background: var(--backdrop);
    font-family: "Lato", sans-serif;
    position: relative;
  }
  .card {
    position: absolute;
    width: 520px;
    height: 298px;
    background: var(--card-stock);
    box-shadow: 0 6px 18px rgba(0,0,0,0.35);
    overflow: hidden;
  }
  .card-front { left: 50px; top: 210px; background: var(--card-edge); }
  .card-back { left: 630px; top: 210px; }

  /* Front */
  .front-panel {
    position: absolute;
    inset: 22px 24px;
    background: var(--front-blue);
    display: flex;
    align-items: center;
    justify-content: center;
  }
  .front-lockup { display: flex; align-items: center; gap: 12px; }
  .lockup-square { width: 26px; height: 26px; border: 2px solid var(--white); }
  .lockup-text { display: flex; flex-direction: column; }
  .lockup-name {
    font-family: "Oswald", sans-serif;
    font-weight: 500;
    font-size: 30px;
    letter-spacing: 0.5px;
    color: var(--white);
    line-height: 1;
  }
  .lockup-roles {
    font-size: 8.5px;
    color: var(--white);
    margin-top: 4px;
    letter-spacing: 0.2px;
    white-space: nowrap;
  }

  /* Back */
  .back-corner-panel {
    position: absolute; left: 0; top: 0;
    width: 46px; height: 128px;
    background: var(--panel-grey);
  }
  .back-left-bar {
    position: absolute; left: 0; top: 128px;
    width: 46px; height: 22px;
    background: var(--brand-blue);
  }
  .back-side-square {
    position: absolute; right: 0; top: 80px;
    width: 32px; height: 38px;
    background: var(--panel-grey);
  }
  .back-right-bar {
    position: absolute; right: 0; top: 190px;
    width: 272px; height: 28px;
    background: var(--brand-blue);
  }
  .back-name {
    position: absolute; right: 38px; top: 50px;
    text-align: right;
    white-space: nowrap;
  }
  .back-name h1 {
    font-family: "Oswald", sans-serif;
    font-weight: 500;
    font-size: 23px;
    color: var(--brand-blue);
    letter-spacing: 0.3px;
    line-height: 1;
    text-transform: uppercase;
  }
  .back-name p { font-size: 9px; color: var(--ink); margin-top: 3px; }
  .contact-list {
    position: absolute;
    font-size: 12.5px;
    line-height: 18px;
    color: var(--ink-soft);
    list-style: none;
    white-space: nowrap;
  }
  .contact-list b { color: var(--ink); font-weight: 700; }
  .contact-licensing { left: 78px; top: 178px; }
  .contact-online { left: 248px; top: 234px; }
</style>
</head>
<body>
  <section class="card card-front" aria-label="Card front">
    <div class="front-panel">
      <div class="front-lockup">
        <span class="lockup-square" aria-hidden="true"></span>
        <div class="lockup-text">
          <span class="lockup-name">MARCUS WHITLEY</span>
          <span class="lockup-roles">Broker • Mortgage Loan Originator • Notary Public</span>
        </div>
      </div>
    </div>
  </section>

  <section class="card card-back" aria-label="Card back">
    <div class="back-corner-panel"></div>
    <div class="back-left-bar"></div>
    <div class="back-side-square"></div>
    <div class="back-right-bar"></div>
    <div class="back-name">
      <h1>Marcus Whitley, SFR</h1>
      <p>Broker • Mortgage Loan Originator • Notary Public</p>
    </div>
    <ul class="contact-list contact-licensing">
      <li><b>DRE License</b> #07329184</li>
      <li><b>NMLS</b> 581706</li>
      <li><b>Cell</b> 714-552-0718</li>
      <li><b>Fax</b> 888-417-2965</li>
    </ul>
    <ul class="contact-list contact-online">
      <li><b>E-mail</b> mw@marcuswhitleyhomes.example</li>
      <li><b>Website</b> www.marcuswhitleyhomes.example</li>
    </ul>
  </section>
</body>
</html>
```